Lumen Kinetics Web Design Project

We need to update our web design for our company. Lumen Kinetics™ is a series of Development (Training) Programs that we deliver both for the General Public as well as Corporate Business.

Much of the content needs a refresh but we are keen to get some thoughts now on design and layout, predominantly front page. Happy to take any comments on the content if you think that is relevant as well.

We might look to move the current video clip and bring a more generic 'inspirational' clip to the front page. A good example of this is www.mindcraftoz.example.au

Our courses have a very similar market to Gerald Whitcombe type courses ... both General Public and Corporate business.

Refer our website www.lumenkinetics.example.com

Target Market(s)

General Public as well as Corporate Business. Courses are designed for all. Gerald Whitcombe would be a good 'feel' for what we do.

Industry/Entity Type

Business

Requirements
Must have
• Must have a 'leading edge' type feel to it.
Must look professional.

```html
<!DOCTYPE html>
<html lang="en">
<head>
<meta charset="utf-8">
<title>Lumen Kinetics</title>
<link rel="stylesheet" href="https://fonts.googleapis.com/css2?family=Oswald:wght@300;400;500;600;700&family=Open+Sans:wght@400;600;700&family=Montserrat:wght@400;500;600&family=Lora:ital@1&display=swap">
<style>
:root{
  --brand:#1c6cb8;
  --brand-dark:#0b4a8a;
  --hero-top:#1469b4;
  --hero-bottom:#0a4f93;
  --headline:#7fd6f7;
  --ink:#222;
  --muted:#666;
  --accent:#c8461a;
  --grey-band:#e6e7e9;
  --nav-active:#1b64ad;
  --green:#1c8a3a;
  --footer:#123d66;
  --footer-base:#3b2a22;
}
*{box-sizing:border-box;margin:0;padding:0}
html,body{width:754px;height:1200px;overflow:hidden}
body{position:relative;background:#fff;font-family:"Open Sans",Arial,sans-serif;color:var(--ink)}
h1,h2,h3{font-weight:400}
.abs{position:absolute}

/* header */
.site-header{left:0;top:0;width:754px;height:100px;background:linear-gradient(#f4f9fd,#dcebf7)}
.brand{left:88px;top:26px;display:flex;align-items:center;gap:10px}
.brand-name{font-family:"Montserrat",sans-serif;font-weight:500;font-size:25px;line-height:27px;color:var(--brand);width:140px}
.brand-dot{width:14px;height:14px;border-radius:50%;background:var(--brand)}
.social{top:14px;left:565px;display:flex;gap:13px}
.social span{width:19px;height:19px;border-radius:50%;background:#3a94d6;display:block}
.agent{left:503px;top:34px;width:40px;height:52px;border-radius:6px;background:linear-gradient(#e9d7cb,#7b8795)}
.callbox{left:546px;top:38px;width:120px;height:50px;border:2px solid var(--brand);border-radius:4px;background:#fff;overflow:hidden}
.callbox .label{background:var(--brand);color:#fff;font-family:"Montserrat",sans-serif;font-size:11px;line-height:16px;padding:1px 6px;letter-spacing:.5px}
.callbox .num{font-family:"Oswald",sans-serif;font-weight:600;font-size:15px;letter-spacing:-.2px;color:var(--brand-dark);padding:0 5px;line-height:28px;white-space:nowrap}

/* nav */
.main-nav{left:0;top:100px;width:754px;height:24px;background:#fff;border-top:1px solid #c9d3dc;border-bottom:1px solid #c9d3dc}
.main-nav ul{position:absolute;left:88px;top:-1px;display:flex;list-style:none;height:24px}
.main-nav li{font-family:"Oswald",sans-serif;font-size:10.5px;color:#333;padding:0 12px;line-height:24px;border-right:1px solid #ccc}
.main-nav li:first-child{border-left:1px solid #ccc}
.main-nav li.active{background:var(--nav-active);color:#fff;font-weight:500;padding:0 14px}

/* hero */
.hero{left:0;top:124px;width:754px;height:266px;background:radial-gradient(ellipse at 40% 40%,var(--hero-top),var(--hero-bottom))}
.video{left:88px;top:30px;width:325px;height:205px;background:#fff;padding:7px;box-shadow:0 2px 6px rgba(0,0,0,.35)}
.video-screen{width:100%;height:170px;background:radial-gradient(ellipse at 55% 45%,#3a86d8,#0f3f8a)}
.video-bar{width:100%;height:14px;background:#1b1b1b;position:relative}
.video-bar::before{content:"";position:absolute;left:4px;right:4px;top:1px;height:2px;background:#555}
.play{left:145px;top:75px;width:30px;height:22px;background:#d9241e;border-radius:5px}
.play::after{content:"";position:absolute;left:12px;top:6px;border-left:9px solid #fff;border-top:5px solid transparent;border-bottom:5px solid transparent}
.headline{left:425px;top:20px;font-family:"Oswald",sans-serif;font-weight:700;font-size:20px;line-height:29px;color:var(--headline);letter-spacing:.3px}
.hero-rule{left:425px;top:152px;width:240px;height:1px;background:rgba(255,255,255,.25)}
.tagline{left:425px;top:166px;font-family:"Oswald",sans-serif;font-size:10px;color:#fff;letter-spacing:.2px}
.btn-learn{left:425px;top:199px;width:73px;height:27px;border:2px solid #fff;background:var(--green);color:#fff;font-family:"Oswald",sans-serif;font-size:11px;text-align:center;line-height:23px;box-shadow:0 1px 3px rgba(0,0,0,.4)}

/* programs */
.programs{left:0;top:390px;width:754px;height:178px;background:var(--grey-band)}
.program{top:30px;width:131px;text-align:center}
.program .photo{height:100px;border:1px solid #999;box-shadow:0 3px 5px rgba(0,0,0,.35)}
.program p{font-size:12px;margin-top:12px;color:#111}

/* welcome */
.welcome-title{left:88px;top:592px;font-family:"Montserrat",sans-serif;font-weight:400;font-size:21px;color:var(--brand)}
.intro{left:88px;top:626px;width:372px;font-size:8.5px;line-height:14px;color:var(--muted)}
.contact-bar{left:88px;top:684px;width:372px;height:34px;background:#2e2e2e;color:#fff;padding:3px 7px}
.contact-bar strong{font-family:"Montserrat",sans-serif;font-weight:500;font-size:14px;display:block;line-height:17px}
.contact-bar small{display:block;font-size:8px;line-height:10px;padding-left:2px}
.benefits{left:98px;top:726px;list-style:none;font-size:8.5px;color:#555}
.benefits li{line-height:20.5px;padding-left:12px;position:relative}
.benefits li::before{content:"›";position:absolute;left:0;color:#e36c09;font-weight:700;font-size:12px;line-height:19px}
.experience-title{left:88px;top:850px;font-family:"Oswald",sans-serif;font-weight:300;font-size:15px;color:#222}
.steps{left:88px;top:883px;list-style:none}
.steps li{display:flex;align-items:center;height:36px;font-family:"Oswald",sans-serif;font-weight:300;font-size:11.5px;color:#333}
.steps .n{width:31px;height:31px;border-radius:50%;background:#e4e4e4;border:1px dashed #bbb;text-align:center;line-height:30px;font-size:15px;margin-right:12px;color:#222}
.steps em{font-style:normal;color:var(--accent);margin-left:4px}

/* sidebar */
.sidebar{left:471px;top:578px;width:195px;height:480px;background:#fff;box-shadow:0 0 5px rgba(0,0,0,.25)}
.side-title{left:9px;width:176px;font-family:"Oswald",sans-serif;font-weight:300;font-size:16px;color:var(--brand);border-bottom:2px solid var(--brand);padding-bottom:1px}
.quote{left:9px;top:48px;width:176px;height:102px;border:1px solid #ddd;padding:4px}
.quote div{border:1px solid #e5e5e5;height:100%;padding:4px 6px 0 20px;font-family:"Lora",serif;font-style:italic;font-size:8px;line-height:13px;color:#555;position:relative}
.quote div::before{content:"“";position:absolute;left:5px;top:-4px;font-size:26px;color:#bbb}
.client{left:40px;top:164px;font-size:8px;font-weight:600;color:var(--brand)}
.sep{left:0;width:195px;height:1px;background:#e2e2e2}
.subscribe{left:9px;top:225px;width:176px;height:22px;border:1px solid #ccc;border-radius:3px;overflow:hidden}
.subscribe span{position:absolute;right:0;top:0;width:54px;height:20px;background:#333;color:#fff;font-family:"Oswald",sans-serif;font-size:10px;text-align:center;line-height:20px}
.news{left:9px;width:150px;font-size:8px;line-height:13.5px;color:#444}
.news time{display:block;color:var(--brand);font-size:7px;font-weight:600}

/* footer */
.footer{left:0;top:1088px;width:754px;height:75px;background:linear-gradient(#1d4f80,var(--footer))}
.f-col{top:12px;color:#fff}
.f-col h3{font-family:"Montserrat",sans-serif;font-weight:400;font-size:14px;letter-spacing:.5px;border-bottom:1px solid rgba(255,255,255,.5);padding-bottom:2px;display:flex;align-items:center;gap:6px;width:120px}
.f-col p{font-family:"Montserrat",sans-serif;font-size:8.5px;line-height:13px;margin-top:6px;font-weight:600}
.footer-base{left:0;top:1163px;width:754px;height:37px;background:var(--footer-base);color:#fff;text-align:center}
.footer-base ul{list-style:none;display:flex;justify-content:center;gap:25px;font-size:8px;padding-top:5px}
.footer-base p{font-size:7px;margin-top:4px}
</style>
</head>
<body>

<header class="site-header abs">
  <div class="brand abs"><span class="brand-name">Lumen Kinetics™</span><span class="brand-dot"></span></div>
  <div class="social abs" aria-label="Social links"><span></span><span></span><span></span></div>
  <div class="agent abs" role="img" aria-label="Photo of a support agent with headset"></div>
  <div class="callbox abs"><div class="label">CALL US ON</div><div class="num">61(0) 400 555 019</div></div>
</header>

<nav class="main-nav abs">
  <ul>
    <li class="active">Home</li><li>Lumen Kinetics™</li><li>About Us</li><li>Our Programs</li><li>Events</li><li>Our Products</li><li>Articles &amp; Resources</li><li>Contact Us</li>
  </ul>
</nav>

<section class="hero abs">
  <div class="video abs">
    <div class="video-screen" role="img" aria-label="Intro video still in blue tones"></div>
    <div class="video-bar"></div>
    <div class="play abs"></div>
  </div>
  <h1 class="headline abs">IF THERE IS ONE THING<br>YOU DO THIS YEAR.....<br>MAKE SURE IT'S<br>LUMEN KINETICS™</h1>
  <div class="hero-rule abs"></div>
  <p class="tagline abs">A NEW WAY OF THINKNG TO CREAT, A NEW WAY OF BEING</p>
  <div class="btn-learn abs">LEARN MORE</div>
</section>

<section class="programs abs">
  <div class="program abs" style="left:89px"><div class="photo" role="img" aria-label="Community group seated in a circle" style="background:linear-gradient(#6d6a5e,#3e3a33)"></div><p>Community Training</p></div>
  <div class="program abs" style="left:238px"><div class="photo" role="img" aria-label="Children's sports team on grass" style="background:linear-gradient(#b98a6a,#4f7a3a)"></div><p>Children Training</p></div>
  <div class="program abs" style="left:386px"><div class="photo" role="img" aria-label="Dog training session outdoors" style="background:linear-gradient(#5f6c7a,#3e5a2e)"></div><p>Animals Training</p></div>
  <div class="program abs" style="left:535px"><div class="photo" role="img" aria-label="Business team in an office" style="background:linear-gradient(#d7d3cf,#4a4e5a)"></div><p>Busimessman Training</p></div>
</section>

<h2 class="welcome-title abs">WELCOME TO LUMEN KINETICS</h2>
<p class="intro abs">Lumen Kinetics™ is a leading edge model which introduces a new lens to view yourself and the world you operate within.&nbsp; Lumen Kinetics™ is for everyone.&nbsp; It's all about Transformation and Skills for Life.</p>
<div class="contact-bar abs"><strong>Contact Us Now</strong><small>you will never look back!</small></div>
<ul class="benefits abs">
  <li>Improve your health and wellbeing</li>
  <li>Create a new fun and healthy culture</li>
  <li>Learn new ways to manage stress and create balance in your life</li>
  <li>Enhance your communication skills and strengthen your relationships</li>
  <li>Learn new ways to Transform and create all that you have ever wanted.</li>
</ul>
<h3 class="experience-title abs">EXPERIENCE FOR YOURSELF</h3>
<ol class="steps abs">
  <li><span class="n">1</span>LUMEN KINETICS™ <em>FOR YOU</em></li>
  <li><span class="n">2</span>LUMEN KINETICS™ <em>FOR CHILDREN AND SCHOOLS</em></li>
  <li><span class="n">3</span>LUMEN KINETICS™ <em>FOR BUSINESS</em></li>
  <li><span class="n">4</span>LUMEN KINETICS™ <em>FOR ANIMALS</em></li>
  <li><span class="n">5</span>LUMEN KINETICS™ <em>FOR COMMUNITY</em></li>
</ol>

<aside class="sidebar abs">
  <h3 class="side-title abs" style="top:16px">TESTIMONIAL</h3>
  <div class="quote abs"><div>Lorem Ipsum is simply dummy text of the printing and typesetting industry. Lorem Ipsum has been the industry's standard dummy text ever since the 1500s, printer took a galley of type.</div></div>
  <p class="client abs">Client's Name</p>
  <div class="sep abs" style="top:182px"></div>
  <h3 class="side-title abs" style="top:192px">NEWSLETTER</h3>
  <div class="subscribe abs"><span>SUBSCRIBE</span></div>
  <div class="sep abs" style="top:265px"></div>
  <h3 class="side-title abs" style="top:274px">LATEST NEWS</h3>
  <div class="news abs" style="top:309px"><time>31 JUNE 2013</time>It is a long established fact that a reader will be distracted by the readable content of a page when looking at</div>
  <div class="sep abs" style="top:374px;left:9px;width:176px"></div>
  <div class="news abs" style="top:387px"><time>31 JUNE 2013</time>It is a long established fact that a reader will be distracted by the readable content of a page when looking at</div>
</aside>

<footer class="footer abs">
  <div class="f-col abs" style="left:88px">
    <h3><svg width="9" height="12" viewBox="0 0 9 12"><path d="M4.5 0A4.5 4.5 0 0 0 0 4.5C0 8 4.5 12 4.5 12S9 8 9 4.5A4.5 4.5 0 0 0 4.5 0z" fill="#fff"/><circle cx="4.5" cy="4.5" r="1.7" fill="#1d4f80"/></svg>ADDRESS</h3>
    <p>PO BOX 118, HARBOUR STREET WEST<br>VIC 8010 AUSTRALIA</p>
  </div>
  <div class="f-col abs" style="left:320px">
    <h3><svg width="8" height="12" viewBox="0 0 8 12"><path d="M6 0C2 1 0 3.5 0 6s2 5 6 6l1.5-2.5L5.5 8C4 7.5 3.5 6.8 3.5 6S4 4.5 5.5 4l2-1.5z" fill="#fff"/></svg>PHONE NO</h3>
    <p>+61 (3) 9000 5521<br>+61 (0) 400 555 019</p>
  </div>
  <div class="f-col abs" style="left:553px">
    <h3><svg width="12" height="9" viewBox="0 0 12 9"><rect width="12" height="9" fill="#fff"/><path d="M0 0l6 5 6-5" fill="none" stroke="#1d4f80" stroke-width="1.2"/></svg>EMAIL</h3>
    <p style="font-weight:400">info@lumenkinetics.example.com</p>
  </div>
</footer>
<div class="footer-base abs">
  <ul><li>Home</li><li>Lumen Kinetics™</li><li>About Us</li><li>Our Programs</li><li>Events</li><li>Our Products</li><li>Articles &amp; Resources</li><li>Contact Us</li></ul>
  <p>Copyright © 2013&nbsp; Lumen Kinetics.&nbsp; All Rights Reserved.</p>
</div>

</body>
</html>
```